Business card for Eyelash extension salon in Beverly Hills,California USA

We need new business card for our salon in Beverly Hills. The salon name is 'Lumarra' . We would like to have...Business name: Lumarra Name of person: will provide later Address 6128 N.Corbel Ridge Blvd Marenford Hills , CA 90999 Phone: will provide later (Text only) Web: www.lumarrastudio-example.com Pictogrid icon, Friendvale icon follow us for seasonal campaign and news @lumarrastudioexample Design should look elegant, high-end, clean, simple, cohesive with my brand. Please refer my brand board. Business name color will be metallic bronzy color. Im thinking grey background or white background. Thanks

Target Market(s)

25-35. Gender neutral. People who are in Entertainment business industry.
This is High-end Eyelash extension salon in Beverly Hills

Industry/Entity Type

Beauty Salon

Contact Information for Business Card

Business name: Lumarra
Name of person: will provide later
Address 6128 N.Corbel Ridge Blvd Marenford Hills , CA 90999
Phone: will provide later (Text only)
Web: www.lumarrastudio-example.com
Pictogrid icon, Friendvale icon
follow us for seasonal campaign and news @lumarrastudioexample

Requirements
Must have
• Beautiful, elegant, clean and simple look but very attractive and modern
Should not have
• We don't like too clutter, too busy designs.

```html
<!DOCTYPE html>
<html lang="en">
<head>
<meta charset="utf-8">
<title>Lumarra – Business Card</title>
<link rel="stylesheet" href="https://fonts.googleapis.com/css2?family=Nunito:wght@500;600&family=Playfair+Display:ital,wght@1,800&display=swap">
<style>
  :root {
    --page: #ffffff;
    --card-grey: #abbec6;
    --brand-blue: #0b1ff2;
    --ink-blue: #1a20d8;
    --bronze-dark: #8a5410;
    --bronze-mid: #cf8d1c;
    --bronze-light: #f6ee92;
    --bronze-name: #c8913a;
  }
  * { box-sizing: border-box; margin: 0; padding: 0; }
  html, body {
    width: 1200px; height: 900px; overflow: hidden;
    background: var(--page);
  }
  .canvas { position: relative; width: 1200px; height: 900px; }

  .card {
    position: absolute; left: 333px; width: 532px; height: 296px;
    background: var(--card-grey);
    font-family: "Nunito", Arial, sans-serif;
    color: var(--ink-blue);
  }
  .card--front { top: 101px; }
  .card--back { top: 433px; }

  .bronze-band {
    position: absolute; left: 0; width: 100%; height: 18px;
    background: linear-gradient(90deg, var(--bronze-dark) 0%, var(--bronze-mid) 22%, var(--bronze-light) 50%, var(--bronze-mid) 78%, var(--bronze-dark) 100%);
  }
  .bronze-band--top { top: 0; }
  .bronze-band--bottom { bottom: 0; }

  .brand-panel {
    position: absolute; background: var(--brand-blue); border-radius: 22px;
    display: flex; align-items: center; justify-content: center;
  }
  .brand-name {
    font-family: "Nunito", Arial, sans-serif; font-weight: 600;
    color: var(--bronze-name); letter-spacing: 1px;
  }
  .card--front .brand-panel { left: 40px; top: 33px; width: 196px; height: 119px; }
  .card--front .brand-name { font-size: 38px; }
  .card--back .brand-panel { left: 129px; top: 64px; width: 274px; height: 167px; border-radius: 28px; }
  .card--back .brand-name { font-size: 54px; }

  .holder {
    position: absolute; left: 329px; top: 60px;
    font-family: "Playfair Display", Georgia, serif; font-style: italic; font-weight: 800;
    color: var(--ink-blue); white-space: nowrap;
  }
  .holder__name { font-size: 30px; line-height: 36px; letter-spacing: 1.5px; }
  .holder__role { font-size: 17px; line-height: 20px; letter-spacing: 1.2px; }

  .contact {
    position: absolute; display: flex; align-items: flex-start; gap: 8px;
    font-size: 17px; line-height: 21px; font-weight: 500; white-space: nowrap;
    letter-spacing: 0.2px;
  }
  .contact svg { flex: none; margin-top: 4px; }
  .contact--address { left: 29px; top: 171px; }
  .contact--phone { left: 29px; top: 220px; }
  .contact--pictogrid { left: 304px; top: 171px; }
  .contact--friendvale { left: 304px; top: 196px; }
  .contact--email { left: 304px; top: 221px; }
  .contact--web { left: 149px; top: 243px; }
  .contact--small svg { margin-top: 5px; }
</style>
</head>
<body>
<main class="canvas">

  <section class="card card--front" aria-label="Business card front">
    <div class="bronze-band bronze-band--top"></div>
    <div class="brand-panel"><span class="brand-name">Lumarra</span></div>

    <div class="holder">
      <p class="holder__name">Your Name</p>
      <p class="holder__role">Your Position</p>
    </div>

    <div class="contact contact--address">
      <svg width="13" height="13" viewBox="0 0 14 14" aria-hidden="true"><circle cx="7" cy="7" r="6" fill="none" stroke="currentColor" stroke-width="1.3"/><path d="M7 3.5a2.3 2.3 0 0 0-2.3 2.3C4.7 7.6 7 10.5 7 10.5s2.3-2.9 2.3-4.7A2.3 2.3 0 0 0 7 3.5z" fill="currentColor"/></svg>
      <span>6128 N.Corbel Ridge Blvd<br>Marenford Hills , CA 90999</span>
    </div>
    <div class="contact contact--phone">
      <svg width="13" height="13" viewBox="0 0 14 14" aria-hidden="true"><circle cx="7" cy="7" r="6" fill="none" stroke="currentColor" stroke-width="1.3"/><path d="M4.6 3.8l1.3-.2.7 1.7-.8.7a4.6 4.6 0 0 0 2.2 2.2l.7-.8 1.7.7-.2 1.3c-3 .3-5.9-2.6-5.6-5.6z" fill="currentColor"/></svg>
      <span>+1 555 - 555- 0147</span>
    </div>

    <div class="contact contact--small contact--pictogrid">
      <svg width="11" height="11" viewBox="0 0 12 12" aria-hidden="true"><circle cx="6" cy="6" r="5.5" fill="currentColor"/></svg>
      <span>Follow us on Pictogrid</span>
    </div>
    <div class="contact contact--small contact--friendvale">
      <svg width="11" height="11" viewBox="0 0 12 12" aria-hidden="true"><circle cx="6" cy="6" r="5" fill="none" stroke="currentColor" stroke-width="1.3"/></svg>
      <span>Follow us on Friendvale</span>
    </div>
    <div class="contact contact--small contact--email">
      <svg width="11" height="11" viewBox="0 0 12 12" aria-hidden="true"><circle cx="6" cy="6" r="5.5" fill="currentColor"/><rect x="3" y="4" width="6" height="4" fill="none" stroke="#abbec6" stroke-width="0.9"/><path d="M3 4l3 2.2L9 4" fill="none" stroke="#abbec6" stroke-width="0.9"/></svg>
      <span>Follow us on Email</span>
    </div>
    <div class="contact contact--small contact--web">
      <svg width="12" height="12" viewBox="0 0 12 12" aria-hidden="true"><circle cx="6" cy="6" r="5.5" fill="currentColor"/><ellipse cx="6" cy="6" rx="2.2" ry="5" fill="none" stroke="#abbec6" stroke-width="0.8"/><path d="M1 6h10" stroke="#abbec6" stroke-width="0.8"/></svg>
      <span>www.lumarrastudio-example.com</span>
    </div>

    <div class="bronze-band bronze-band--bottom"></div>
  </section>

  <section class="card card--back" aria-label="Business card back">
    <div class="bronze-band bronze-band--top"></div>
    <div class="brand-panel"><span class="brand-name">Lumarra</span></div>
    <div class="bronze-band bronze-band--bottom"></div>
  </section>

</main>
</body>
</html>
```